National Human Immunology Network Needs a Brochure DesignBrochure Design Project

We need a brochure design for a new Canadian network called VEKO. VEKO stands for "VRSL Cellular Defence Alliance". (VRSL is the Northfield Councils of Medical Inquiry and is the funder of the network).

The VRSL Cellular Defence Alliance (VEKO) is a resource network that facilitates, promotes and enhances research in human immunology and its translation into clinical care and public policy. VEKO is an inclusive National Network with International projections that will act as a coordinating resource for investigators working in different aspects of Human Immunology. As a research network, VEKO will operate as a resource “umbrella” network, facilitating communication between nodes, each with their specialized expertise in human immunology,
collaboration and knowledge exchange.

We have a VEKO logo already designed as well as the text to be used in the brochure. In addition we should include the VRSL logo somewhere on the brochure, but it does need to be front and centre. Thinking that a tri-fold brochure would work best.

Target Market(s)

Researchers, politicians, lay public

Industry/Entity Type

Communication

Requirements
Must have
• Must use logo provided.

```html
<!DOCTYPE html>
<html lang="en">
<head>
<meta charset="utf-8">
<title>VEKO Tri-fold Brochure</title>
<link rel="stylesheet" href="https://fonts.googleapis.com/css2?family=Roboto:wght@700&family=Roboto+Condensed:wght@300;400;700&display=swap">
<style>
  :root {
    --red: #c0202a;
    --red-dark: #a3161f;
    --ink: #3a3a3a;
    --ink-soft: #5a5a5a;
    --ink-light: #8a8a8a;
    --paper: #ffffff;
    --paper-grey: #ececec;
    --stage: #1c2533;
  }
  * { box-sizing: border-box; margin: 0; padding: 0; }
  html, body { width: 1200px; height: 817px; overflow: hidden; }
  body {
    background: var(--stage);
    font-family: "Roboto Condensed", "Arial Narrow", sans-serif;
    color: var(--ink);
    position: relative;
  }

  /* ---------- shared ---------- */
  .band { position: absolute; left: 0; right: 0; background: var(--red); }
  .band--top { top: 0; height: 22px; }
  .band--bottom { bottom: 0; height: 22px; }

  .brand { display: flex; align-items: flex-start; gap: 12px; }
  .brand__square { width: 22px; height: 22px; background: var(--red); flex: none; margin-top: 4px; }
  .brand__name {
    font-family: "Roboto", Arial, sans-serif;
    font-weight: 700;
    color: var(--ink-soft);
    text-transform: uppercase;
    line-height: 1.02;
  }

  /* ---------- front cover ---------- */
  .cover {
    position: absolute; left: 40px; top: 58px;
    width: 330px; height: 700px;
    background: var(--paper);
    overflow: hidden;
  }
  .cover__masthead { position: absolute; top: 22px; left: 0; right: 0; height: 140px; }
  .cover .brand { position: absolute; left: 28px; top: 34px; }
  .cover .brand__square { width: 28px; height: 28px; }
  .cover .brand__name { font-size: 23px; }
  .cover__notch { position: absolute; top: 150px; left: 0; width: 330px; height: 42px; z-index: 2; }
  .cover__photo {
    position: absolute; top: 162px; left: 0; right: 0; bottom: 22px;
    background: linear-gradient(170deg, #d9ddd6 0%, #b9bfb4 22%, #1d1b1b 40%, #2a2422 58%, #c9a48c 66%, #b8242c 78%, #9c1c22 100%);
  }

  /* ---------- inside spread ---------- */
  .spread {
    position: absolute; left: 410px; top: 58px;
    width: 750px; height: 700px;
    background: var(--paper-grey);
    overflow: hidden;
  }
  .panel { position: absolute; top: 22px; bottom: 22px; width: 250px; }
  .panel--photo { left: 0; background: var(--paper); }
  .panel--aims { left: 250px; background: linear-gradient(90deg, #e6e6e6, #f2f2f2 30%); }
  .panel--team { left: 500px; background: linear-gradient(90deg, #e4e4e4, #f0f0f0 30%); }

  .panel__photo {
    position: absolute; inset: 0 0 110px 0;
    background: linear-gradient(160deg, #eef0f2 0%, #c9d3de 22%, #8aa6cc 34%, #a58a74 52%, #e4e6e8 72%, #ffffff 100%);
  }
  .panel--photo .brand { position: absolute; left: 22px; bottom: 24px; }
  .panel--photo .brand__name { font-size: 15px; }

  .panel__content { position: absolute; left: 22px; right: 18px; }
  .heading {
    font-weight: 700; font-size: 14px; text-transform: uppercase;
    color: #222; margin-bottom: 3px;
  }
  .copy { font-size: 11.2px; line-height: 1.32; font-weight: 400; color: var(--ink); }
  .list { list-style: none; font-size: 11.2px; line-height: 1.32; }
  .list--bullet li::before { content: "\2022  "; }

  .aims { top: 26px; }
  .aims .list + .heading { margin-top: 16px; }
  .accomplish { top: 470px; color: var(--ink-light); }
  .accomplish .heading { font-size: 10px; color: var(--ink-light); font-weight: 700; }
  .accomplish .copy, .accomplish .list { font-size: 9px; line-height: 1.3; font-weight: 300; color: var(--ink-light); }

  /* right panel flows top to bottom so nothing overlaps */
  .panel--team { display: flex; flex-direction: column; padding-top: 22px; }
  .panel--team .brand { margin-left: 18px; }
  .panel--team .brand__name { font-size: 17px; }
  .team { margin: 20px 16px 0 20px; }
  .team .heading { font-size: 12px; margin-bottom: 2px; }
  .team .list { font-size: 9.8px; font-weight: 300; line-height: 1.42; }
  .team .list + .heading { margin-top: 12px; }
  .note { margin: 10px 12px 0 20px; font-size: 7.2px; line-height: 1.3; font-style: italic; color: var(--ink-light); font-weight: 300; }

  .next-steps {
    margin: 8px 0 0 2px; height: 38px; flex: none;
    background: var(--red);
    border-top: 2px solid var(--red-dark);
    color: #fff; font-weight: 700; font-size: 18px;
    padding: 7px 0 0 14px; text-transform: uppercase;
  }
  .next-copy { margin: 12px 16px 0 20px; font-size: 10.2px; line-height: 1.36; }
</style>
</head>
<body>

  <!-- Front cover -->
  <section class="cover" aria-label="Front cover">
    <div class="band band--top"></div>
    <header class="cover__masthead">
      <div class="brand">
        <span class="brand__square"></span>
        <span class="brand__name">VRSL<br>Cellular<br>Defence<br>Alliance</span>
      </div>
    </header>
    <svg class="cover__notch" viewBox="0 0 330 42" aria-hidden="true">
      <polygon points="0,0 330,0 330,12 92,12 70,34 48,12 0,12" fill="#ffffff"/>
      <polyline points="0,12 48,12 70,34 92,12 330,12" fill="none" stroke="#c0202a" stroke-width="4"/>
    </svg>
    <div class="cover__photo" role="img" aria-label="Photograph of a smiling young woman in a red top tossing her long dark hair"></div>
    <div class="band band--bottom"></div>
  </section>

  <!-- Inside spread -->
  <section class="spread" aria-label="Inside spread">
    <div class="band band--top"></div>

    <article class="panel panel--photo">
      <div class="panel__photo" role="img" aria-label="Photograph of a researcher in blue gloves holding a pipette over a sample tube"></div>
      <div class="brand">
        <span class="brand__square"></span>
        <span class="brand__name">VRSL<br>Cellular<br>Defence<br>Alliance</span>
      </div>
    </article>

    <article class="panel panel--aims">
      <div class="panel__content aims">
        <h2 class="heading">Specific Aims:</h2>
        <ul class="list list--bullet">
          <li>To be a source of standardized protocols for human immunology research;</li>
          <li>To facilitate access to research material and technologies, and to expedite regulatory processes;</li>
          <li>To engage national and international human immunology stakeholders to promote research in human immunology; and</li>
          <li>To lead the development of activities of knowledge dissemination in human immunology at national and international levels.</li>
        </ul>
        <h2 class="heading">Deliverables:</h2>
        <ol class="list">
          <li>1. To standardize protocols for human sample processing and sharing;</li>
          <li>2. To facilitate access to research material and reagents through formalized collaborations;</li>
          <li>3. To expedite ethical and biosafety protocols for human immunology research;</li>
          <li>4. To organize an Annual International Conference on human infection and immunity;</li>
          <li>5. To provide linkage between the Canadian human immunology research community and international organization-based initiatives in human immunology research.</li>
        </ol>
      </div>

      <div class="panel__content accomplish">
        <h2 class="heading">Accomplishments:</h2>
        <p class="copy">In its first year of operation, VEKO has made significant strides in the establishment of the network. Accomplishments to date include:</p>
        <ul class="list list--bullet">
          <li>Establishment and set-up of the administrative coordinating node</li>
          <li>Launch of the VEKO website</li>
          <li>Face-to-face meeting of the node leaders in December 2011, and regular monthly teleconference meetings</li>
          <li>Organization of a satellite symposium on "Immune Regulatory Mechanisms in Health &amp; Disease" at IMFED 2012 in Port Aldren in partnership with the Northern Immunology Society</li>
          <li>Formation of an External Advisory Board to provide advice and guidance to the network</li>
        </ul>
      </div>
    </article>

    <article class="panel panel--team">
      <div class="brand">
        <span class="brand__square"></span>
        <span class="brand__name">VRSL<br>Cellular<br>Defence<br>Alliance</span>
      </div>

      <div class="team">
        <h2 class="heading">Structure of VEKO:</h2>
        <ul class="list list--bullet">
          <li>Director of VEKO – Elena Marchetti (Harwick University)</li>
        </ul>
        <h2 class="heading">Nodes &amp; Leaders:</h2>
        <ul class="list list--bullet">
          <li>Seabrook University – Owen Hartley</li>
          <li>Harwick University – Marco Pellegrini</li>
          <li>University of Lakeport – Nadia Wells</li>
          <li>Delmore University – Simon Brandt</li>
          <li>Westvale University* – Ravi Sethi</li>
          <li>University of Prairieton – Glen Haverly</li>
          <li>University of Coastland – Wei Lin Tao</li>
        </ul>
        <h2 class="heading">External Advisory Board</h2>
        <ul class="list list--bullet">
          <li>Dr. Paul Feldman</li>
          <li>Dr. Laura Grady</li>
          <li>Dr. Arthur Tyndall</li>
        </ul>
      </div>
      <p class="note">*Note that Westvale University is the administrative coordinating node for VEKO</p>

      <h2 class="next-steps">Next Steps</h2>
      <p class="copy next-copy">As VEKO moves forward into the second year of its mandate, plans are in the works for expansion of the network. In addition, presence at international meetings and conferences will be ramped up to increase the profile of the network. VEKO plans on organizing community events across the country to inform the public of current research in human immunology. Finally, a focus on providing resources to trainees and fellows in the form of training seminars will also be examined as a possible resource that can be provided by VEKO.</p>
    </article>

    <div class="band band--bottom"></div>
  </section>

</body>
</html>
```